Long Established Local Fencing (not swords) Business needs fresh Business Cards

We need fresh double sided business cards for our Fencing Construction business, we are looking for something with our new logo design added, and maybe a photo background ?
We recently had cards made from Quillmarko and we were horrified with what we got back, the quality was terrible, so am looking for high quality format for good printing company to make.
We install Steelwave, Timber paling, Aluminium Slat Screening, Picket (timber and aluminium) and most other fencing installations.
Our website is brelbanfencing.com.au should you like to learn a bit more.
We do have logo in other formats if required.
We have been in business for over 35 years and we have used this as a "motto" it is on our signage

Industry/Entity Type

Construction

Contact Information for Business Card

Open to ideas, we need 3 x different cards, one generic with no name and 2 x others each with 1 of our bosses name on each, I will put into upload files.

Colors
ec1f27
000000
606060
f5f5f5

Requirements
Must have
• Company Name and Logo
• Address
• Contact details, phone, website, email etc
• Small space to write notes when leaving card at residence
Nice to have
• Our motto "Servicing the Peninsula for over 35 years"

```html
<!DOCTYPE html>
<html lang="en">
<head>
<meta charset="utf-8">
<title>Brelban Fencing – Business Cards</title>
<link href="https://fonts.googleapis.com/css2?family=Lato:wght@400;700&display=swap" rel="stylesheet">
<style>
  :root {
    --brand-red: #ec1f27;
    --card-black: #1c1c1c;
    --mid-grey: #606060;
    --off-white: #f5f5f5;
    --backdrop: #3b322e;
    --edge-red: #b3151c;
  }
  * { margin: 0; padding: 0; box-sizing: border-box; }
  html, body {
    width: 1200px; height: 715px; overflow: hidden;
    background: var(--backdrop);
    font-family: "Lato", Arial, sans-serif;
  }
  .canvas {
    position: relative; width: 1200px; height: 715px;
    display: flex; align-items: center; justify-content: center; gap: 44px;
  }
  .card {
    position: relative; width: 540px; height: 328px;
    background: var(--card-black);
    border-radius: 4px;
    box-shadow: 0 3px 0 var(--edge-red), 0 14px 30px rgba(0,0,0,.45);
    color: var(--off-white);
  }
  .wordmark {
    display: flex; align-items: center; gap: 12px;
    font-weight: 700; color: var(--off-white);
    text-transform: uppercase; letter-spacing: 1px; line-height: 1.05;
  }
  .wordmark__dot {
    width: 16px; height: 16px; border-radius: 50%;
    background: var(--brand-red); flex: none;
  }
  .card--front { display: flex; align-items: center; justify-content: center; }
  .card--front .wordmark { font-size: 40px; }
  .card--back { display: flex; align-items: center; }
  .card--back .brand-side {
    width: 270px; display: flex; justify-content: center;
  }
  .card--back .wordmark { font-size: 30px; gap: 10px; }
  .card--back .wordmark__dot { width: 13px; height: 13px; }
  .divider {
    width: 1px; height: 170px; background: var(--off-white); opacity: .85;
  }
  .contact { padding-left: 30px; font-size: 15px; line-height: 1.45; }
  .contact__name {
    color: var(--brand-red); font-size: 24px; font-weight: 400;
    text-transform: uppercase; letter-spacing: .5px; line-height: 1.1;
  }
  .contact__role { font-size: 14px; margin-bottom: 6px; }
  .contact__row { display: flex; align-items: center; gap: 8px; }
  .contact__row svg { width: 11px; height: 11px; flex: none; }
  .contact__plain { padding-left: 0; }
  .accent { color: var(--brand-red); }
</style>
</head>
<body>
<main class="canvas">
  <section class="card card--front" aria-label="Card front">
    <div class="wordmark"><span class="wordmark__dot"></span><span>Brelban<br>Fencing</span></div>
  </section>

  <section class="card card--back" aria-label="Card back">
    <div class="brand-side">
      <div class="wordmark"><span class="wordmark__dot"></span><span>Brelban<br>Fencing</span></div>
    </div>
    <div class="divider"></div>
    <div class="contact">
      <p class="contact__name">Daniel Harrow</p>
      <p class="contact__role">Director</p>
      <p class="contact__plain">42 Kerrin Street</p>
      <p class="contact__plain">Brelban Nsw 2260</p>
      <p class="contact__row">
        <svg viewBox="0 0 12 12" aria-hidden="true"><path d="M2.5 1 4.5 1 5.3 3.6 4 4.6C4.7 6 6 7.3 7.4 8L8.4 6.7 11 7.5 11 9.5C11 10.3 10.3 11 9.5 11 5 11 1 7 1 2.5 1 1.7 1.7 1 2.5 1Z" fill="var(--brand-red)"/></svg>
        <span>02 4388 2051</span>
      </p>
      <p class="contact__row">
        <svg viewBox="0 0 12 12" aria-hidden="true"><rect x="1" y="2.5" width="10" height="7" rx="1" fill="none" stroke="var(--brand-red)" stroke-width="1.3"/><path d="M1.5 3 6 6.5 10.5 3" fill="none" stroke="var(--brand-red)" stroke-width="1.3"/></svg>
        <span>brelbanfencing@mailnet.com</span>
      </p>
      <p class="contact__row">
        <svg viewBox="0 0 12 12" aria-hidden="true"><circle cx="6" cy="6" r="5" fill="none" stroke="var(--brand-red)" stroke-width="1.2"/><ellipse cx="6" cy="6" rx="2.2" ry="5" fill="none" stroke="var(--brand-red)" stroke-width="1"/><path d="M1 6H11" stroke="var(--brand-red)" stroke-width="1"/></svg>
        <span>www.<span class="accent">brelbanfencing</span>.com.au</span>
      </p>
    </div>
  </section>
</main>
</body>
</html>
```